Velvet Founders Income Blueprint

I need a Mockup Design for a digital course Materials - that is teaching you how to generate money with social media (e.G Glimmerly)
- we are two girls who are teaching but the design should be dark and neutral

- We need to get it same as the picture shows with Mockup
BOX and Thumbnail
- We don't have a real logo yet so it needs to all included with the package design. This designs becomes also the logo in a way.

- It needs to be classy and luxury and shows a BOLD Brand
- we like it very black and dark - mixed with gold
-

Women and Men who want to escape the 9/5

```html
<!DOCTYPE html>
<html lang="en">
<head>
<meta charset="utf-8">
<title>Velvet Founders Income Blueprint – Package Design</title>
<link href="https://fonts.googleapis.com/css2?family=Bodoni+Moda:opsz,wght@6..96,700;6..96,800&family=Josefin+Sans:wght@300;400&display=swap" rel="stylesheet">
<style>
  :root {
    --page: #ffffff;
    --board-dark: #221f20;
    --board-mid: #423e40;
    --gold-light: #ecd97a;
    --gold-deep: #7f702e;
    --ink-white: #ececec;
  }
  * { margin: 0; padding: 0; box-sizing: border-box; }
  html, body { width: 1080px; height: 1200px; overflow: hidden; background: var(--page); }
  .canvas { position: relative; width: 1080px; height: 1200px; }

  .spine, .cover {
    position: absolute;
    top: 60px;
    height: 1080px;
    overflow: hidden;
  }
  .spine {
    left: 60px;
    width: 180px;
    background: linear-gradient(180deg, var(--board-dark) 0%, var(--board-mid) 30%, var(--board-dark) 55%, var(--board-dark) 100%);
    border-right: 1px solid #111;
    text-align: center;
  }
  .cover {
    left: 240px;
    width: 780px;
    background: linear-gradient(135deg, var(--board-dark) 0%, var(--board-mid) 38%, var(--board-dark) 52%, var(--board-mid) 100%);
  }

  .pattern-area { position: absolute; }
  .spine .pattern-area { left: 0; top: 0; width: 180px; height: 300px;
    background: linear-gradient(180deg, rgba(127,112,46,.75), rgba(127,112,46,0)); }
  .cover .pattern-area.top { left: 0; top: 0; width: 240px; height: 130px;
    background: linear-gradient(160deg, rgba(127,112,46,.7), rgba(127,112,46,0)); }
  .cover .pattern-area.bottom { right: 0; bottom: 0; width: 400px; height: 380px;
    background: radial-gradient(ellipse at 80% 80%, rgba(236,217,122,.75), rgba(236,217,122,0) 70%); }

  .spine-title { margin-top: 330px; font-family: "Bodoni Moda", serif; font-weight: 700; color: var(--gold-deep); line-height: 1; }
  .spine-title .word-1 { display: block; font-size: 44px; transform: scaleX(.8); }
  .spine-title .word-2 { display: block; font-size: 28px; transform: scaleX(.8); margin-top: 4px; }
  .spine-subtitle { font-family: "Josefin Sans", sans-serif; font-weight: 300; font-size: 14px; color: var(--ink-white); opacity: .75; letter-spacing: 1px; margin-top: 10px; }
  .spine-copy { font-family: "Josefin Sans", sans-serif; font-weight: 400; font-size: 13px; line-height: 22px; color: var(--gold-deep); text-transform: uppercase; width: 120px; margin: 70px auto 0; }
  .spine-copy + .spine-copy { margin-top: 50px; }

  .brand-mark { position: absolute; left: 330px; top: 200px; display: flex; align-items: center; gap: 12px; }
  .brand-mark .square { width: 40px; height: 40px; background: var(--gold-deep); border-radius: 6px; }
  .brand-mark .name { font-family: "Josefin Sans", sans-serif; font-weight: 400; font-size: 24px; letter-spacing: 3px; color: var(--gold-deep); text-transform: uppercase; }

  .cover-title { position: absolute; left: 80px; top: 400px; font-family: "Bodoni Moda", serif; font-weight: 800; line-height: .9;
    background: linear-gradient(100deg, var(--gold-light) 0%, var(--gold-light) 45%, var(--gold-deep) 60%, var(--gold-deep) 80%, var(--gold-light) 100%);
    -webkit-background-clip: text; background-clip: text; color: transparent; }
  .cover-title .line-1 { display: block; font-size: 150px; letter-spacing: -2px; }
  .cover-title .line-2 { display: block; font-size: 92px; letter-spacing: 4px; margin-top: 20px; }
  .cover-subtitle { position: absolute; left: 84px; top: 680px; font-family: "Josefin Sans", sans-serif; font-weight: 300; font-size: 50px; letter-spacing: 3px; color: var(--ink-white); }
</style>
</head>
<body>
<main class="canvas">
  <section class="spine">
    <div class="pattern-area" role="img" aria-label="Gold geometric square-and-line pattern"></div>
    <h2 class="spine-title"><span class="word-1">VELVET</span><span class="word-2">FOUNDERS</span></h2>
    <p class="spine-subtitle">INCOME BLUEPRINT</p>
    <p class="spine-copy">Lorem ipsum dolor sit amet, consectetuer adipiscing elit, sed diam nonum&shy;my nibh euismod tincidunt ut laoreet dolore magna aliquam</p>
    <p class="spine-copy">Lorem ipsum dolor sit amet, consectetuer adipiscing elit, sed diam nonum&shy;my nibh euismod tincidunt ut laoreet dolore magna aliquam</p>
  </section>

  <section class="cover">
    <div class="pattern-area top" role="img" aria-label="Gold geometric square-and-line pattern"></div>
    <div class="brand-mark"><span class="square"></span><span class="name">Velvet Founders</span></div>
    <h1 class="cover-title"><span class="line-1">VELVET</span><span class="line-2">FOUNDERS</span></h1>
    <p class="cover-subtitle">INCOME BLUEPRINT</p>
    <div class="pattern-area bottom" role="img" aria-label="Gold geometric square-and-line pattern"></div>
  </section>
</main>
</body>
</html>
```